Brave Otter Pet Sitting Postcard

I will be sending these postcards to homes in the neighborhood introducing my pet sitting business.

Include the following on the postcard:
Rosalind Hume
555-318-7294
www.braveotterpetsitting.example
help@braveotterpetsitting.example

```html
<!DOCTYPE html>
<html lang="en">
<head>
<meta charset="utf-8">
<title>Brave Otter Pet Sitting Postcard</title>
<link href="https://fonts.googleapis.com/css2?family=Baloo+2:wght@800&family=Carlito:ital@1&family=Comic+Neue:ital@1&family=Roboto+Condensed:ital,wght@1,700&family=Poppins:wght@500;600&display=swap" rel="stylesheet">
<style>
  :root {
    --navy: #14315a;
    --navy-deep: #0f2747;
    --sky: #5ec3f2;
    --sky-light: #bfe6fb;
    --gold: #f7c95b;
    --brown: #9a5a3a;
    --beige: #f3e3d2;
    --red: #e0323c;
    --ink: #2a2a2a;
    --page: #eef0f3;
    --white: #ffffff;
  }
  html, body {
    margin: 0;
    width: 899px;
    height: 1200px;
    overflow: hidden;
    background: var(--page);
  }
  .postcard {
    position: absolute;
    left: 20px;
    top: 314px;
    width: 1005px;
    height: 668px;
    transform: scale(0.855);
    transform-origin: 0 0;
    background: var(--white);
    overflow: hidden;
    box-shadow: 0 4px 14px rgba(0,0,0,.15);
  }
  .backdrop { position: absolute; inset: 0; }
  .photo {
    position: absolute;
    left: 0; top: 190px;
    width: 360px; height: 460px;
    background: linear-gradient(90deg, #a0603c 0%, #b77a52 45%, rgba(230,215,205,.6) 80%, rgba(255,255,255,0) 100%);
  }
  .brand-title {
    position: absolute;
    left: 55px; top: 8px;
    margin: 0;
    font: 800 66px/1 "Baloo 2", sans-serif;
    color: var(--sky);
    letter-spacing: -1px;
  }
  .brand-sub {
    position: absolute;
    left: 482px; top: 52px;
    margin: 0;
    font: italic 48px/1 "Carlito", sans-serif;
    color: var(--gold);
  }
  .question {
    position: absolute;
    left: 200px; top: 218px;
    margin: 0;
    font: italic 25px/1.45 "Comic Neue", cursive;
    color: var(--ink);
  }
  .question span { display: block; }
  .question span + span { padding-left: 62px; }
  .promise {
    position: absolute;
    left: 298px; top: 288px;
    margin: 0;
    font: italic 700 31px/1 "Roboto Condensed", sans-serif;
    color: var(--brown);
  }
  .services {
    position: absolute;
    left: 292px; top: 338px;
    width: 478px; height: 140px;
    border-radius: 0 18px 18px 0;
    background: linear-gradient(90deg, rgba(243,227,210,0) 0%, var(--beige) 8%);
    display: flex;
    gap: 22px;
    padding: 20px 0 0 6px;
    box-sizing: border-box;
  }
  .services ul { list-style: none; margin: 0; padding: 0; }
  .services li {
    font: 500 20.5px/23.5px "Poppins", sans-serif;
    color: var(--navy);
    display: flex; align-items: center; gap: 8px;
  }
  .tick { width: 14px; height: 14px; flex: none; }
  .logo-mark {
    position: absolute;
    right: 22px; top: 248px;
    width: 150px;
    text-align: center;
  }
  .logo-mark .dot {
    width: 110px; height: 110px;
    margin: 0 auto 8px;
    border-radius: 50%;
    border: 3px solid var(--navy);
    box-sizing: border-box;
  }
  .logo-mark .name {
    font: 600 16px/1.2 "Poppins", sans-serif;
    color: var(--navy);
  }
  .doodle {
    position: absolute;
    left: 680px; top: 440px;
    width: 240px; height: 160px;
    border-radius: 14px;
    background: radial-gradient(ellipse at center, #e6ecf4 0%, rgba(230,236,244,0) 72%);
  }
  .sitter {
    position: absolute;
    left: 304px; top: 508px;
    margin: 0;
    font: italic 700 21px/1 "Poppins", sans-serif;
    color: var(--ink);
  }
  .phone-pill {
    position: absolute;
    left: 348px; top: 538px;
    height: 46px;
    padding: 0 22px 0 16px;
    border-radius: 23px;
    background: var(--navy);
    color: var(--white);
    display: flex; align-items: center; gap: 8px;
    font: 600 30px/1 "Poppins", sans-serif;
    letter-spacing: .5px;
  }
  .phone-pill svg { width: 22px; height: 26px; }
  .footer {
    position: absolute;
    left: 130px; bottom: 14px;
    display: flex; gap: 36px;
    font: 600 19.5px/1 "Poppins", sans-serif;
    color: var(--gold);
  }
  .footer .link { display: flex; align-items: center; gap: 14px; }
  .footer svg { width: 28px; height: 24px; }
</style>
</head>
<body>
  <main class="postcard">
    <div class="photo" role="img" aria-label="Photo of a brown mastiff dog looking up at the camera"></div>

    <svg class="backdrop" viewBox="0 0 1005 668" aria-hidden="true">
      <defs>
        <linearGradient id="wave-sky" x1="0" y1="0" x2="1" y2="0">
          <stop offset="0" stop-color="#7fd0f6"/>
          <stop offset="0.6" stop-color="#3fa9e8"/>
          <stop offset="1" stop-color="#2a86d2"/>
        </linearGradient>
        <linearGradient id="wave-glow" x1="0" y1="0" x2="0" y2="1">
          <stop offset="0" stop-color="#d8f1fd"/>
          <stop offset="1" stop-color="#ffffff" stop-opacity="0"/>
        </linearGradient>
      </defs>
      <path d="M0,0 H1005 V0 C880,70 760,120 560,150 C360,180 200,140 0,212 Z" fill="var(--navy)"/>
      <path d="M0,212 C200,140 360,180 560,150 C760,120 880,70 1005,0 V36 C880,110 760,175 560,200 C360,228 200,196 0,262 Z" fill="url(#wave-sky)"/>
      <path d="M0,262 C200,196 360,228 560,200 C760,175 880,110 1005,36 V70 C880,150 760,215 560,232 C360,250 200,230 0,290 Z" fill="url(#wave-glow)"/>
      <path d="M0,606 C250,652 560,650 780,590 C880,562 950,520 1005,492 V668 H0 Z" fill="var(--navy)"/>
      <path d="M0,606 C250,652 560,650 780,590 C880,562 950,520 1005,492" fill="none" stroke="var(--sky)" stroke-width="4"/>
    </svg>

    <h1 class="brand-title">Brave Otter</h1>
    <p class="brand-sub">Pet Sitting</p>

    <p class="question"><span>Do you worry about your pets</span><span>while you are gone from home?</span></p>
    <p class="promise">Let us take that worry away!</p>

    <section class="services">
      <ul>
        <li><svg class="tick" viewBox="0 0 14 14"><circle cx="7" cy="7" r="6" fill="none" stroke="var(--red)" stroke-width="2"/><path d="M4 7.2 6.2 9.3 10 5" fill="none" stroke="var(--red)" stroke-width="2"/></svg>Concierge Services</li>
        <li><svg class="tick" viewBox="0 0 14 14"><circle cx="7" cy="7" r="6" fill="none" stroke="var(--red)" stroke-width="2"/><path d="M4 7.2 6.2 9.3 10 5" fill="none" stroke="var(--red)" stroke-width="2"/></svg>Pet Sitting</li>
        <li><svg class="tick" viewBox="0 0 14 14"><circle cx="7" cy="7" r="6" fill="none" stroke="var(--red)" stroke-width="2"/><path d="M4 7.2 6.2 9.3 10 5" fill="none" stroke="var(--red)" stroke-width="2"/></svg>Almost Overnight</li>
        <li><svg class="tick" viewBox="0 0 14 14"><circle cx="7" cy="7" r="6" fill="none" stroke="var(--red)" stroke-width="2"/><path d="M4 7.2 6.2 9.3 10 5" fill="none" stroke="var(--red)" stroke-width="2"/></svg>Overnight</li>
      </ul>
      <ul>
        <li><svg class="tick" viewBox="0 0 14 14"><circle cx="7" cy="7" r="6" fill="none" stroke="var(--red)" stroke-width="2"/><path d="M4 7.2 6.2 9.3 10 5" fill="none" stroke="var(--red)" stroke-width="2"/></svg>Pet Taxi</li>
        <li><svg class="tick" viewBox="0 0 14 14"><circle cx="7" cy="7" r="6" fill="none" stroke="var(--red)" stroke-width="2"/><path d="M4 7.2 6.2 9.3 10 5" fill="none" stroke="var(--red)" stroke-width="2"/></svg>Pooper Scooper</li>
        <li><svg class="tick" viewBox="0 0 14 14"><circle cx="7" cy="7" r="6" fill="none" stroke="var(--red)" stroke-width="2"/><path d="M4 7.2 6.2 9.3 10 5" fill="none" stroke="var(--red)" stroke-width="2"/></svg>Holiday Schedule</li>
      </ul>
    </section>

    <div class="logo-mark">
      <div class="dot"></div>
      <div class="name">Brave Otter Pet Sitting</div>
    </div>

    <div class="doodle" role="img" aria-label="Line drawing of a dog house, food bowl, bone and paw prints along a dotted path"></div>

    <p class="sitter">Rosalind Hume :-</p>
    <div class="phone-pill">
      <svg viewBox="0 0 22 26"><path d="M6 2 C3 3 2 6 3 10 C5 17 9 22 15 24 C18 25 20 23 20 21 L16 17 L13 19 C10 17 8 14 7 10 L10 8 Z" fill="var(--gold)"/></svg>
      555-318-7294
    </div>

    <footer class="footer">
      <span class="link">
        <svg viewBox="0 0 28 24"><rect x="2" y="4" width="24" height="16" rx="2" fill="var(--gold)"/><path d="M3 5 14 13 25 5" fill="none" stroke="var(--navy)" stroke-width="2"/></svg>
        www.braveotterpetsitting.example
      </span>
      <span class="link">
        <svg viewBox="0 0 28 24"><circle cx="14" cy="12" r="11" fill="var(--gold)"/><path d="M3 12 H25 M14 1 C9 6 9 18 14 23 M14 1 C19 6 19 18 14 23" fill="none" stroke="var(--navy)" stroke-width="1.6"/></svg>
        help@braveotterpetsitting.example
      </span>
    </footer>
  </main>
</body>
</html>
```